Redesign of page from emergency manual

Please redesign this PDF to look better. Please don't include any stock photos. It must be legible. Making some words bold is probably a good idea.

Here are some things I like :

https://tarrowbooks.com.au/collections/frontpage/products/the-plk-v2-ebook

https://img-cd.vostramediafiles.com/qa-ejkwPLOTYY_SuCKbZNu411Qwgjv8YssPxEdzXN93hDkSRjLXK8WmfgbmrJW4ZZ3yUPK=w1052-h592-rw

```html
<!DOCTYPE html>
<html lang="en">
<head>
<meta charset="utf-8">
<title>Hypertension, Acute</title>
<link rel="stylesheet" href="https://fonts.googleapis.com/css2?family=Anton&family=Red+Hat+Display:ital,wght@0,400;0,500;0,700;0,800;1,700;1,800&display=swap">
<style>
  :root {
    --navy: #13285a;
    --green: #86b342;
    --orange: #e8702a;
    --cell: #e7e7e7;
    --ink: #111111;
    --white: #ffffff;
    --backdrop: #adadad;
  }
  * { box-sizing: border-box; margin: 0; padding: 0; }
  html, body { width: 1200px; height: 1117px; overflow: hidden; }
  body { background: var(--backdrop); font-family: "Red Hat Display", sans-serif; color: var(--ink); position: relative; }

  .page { position: absolute; left: 222px; top: 69px; width: 756px; height: 979px; background: var(--white); overflow: hidden; }
  .page > * { position: absolute; }

  .spine { left: 0; top: 0; width: 32px; height: 100%; background: var(--navy); }
  .top-band { left: 50px; top: 0; width: 706px; height: 21px; background: var(--green); }

  .title { left: 86px; top: 42px; font-family: "Anton", sans-serif; font-weight: 400; font-size: 76px; line-height: 1; color: var(--navy); white-space: nowrap; transform: scaleX(1.06); transform-origin: left top; }
  .title .accent { color: var(--green); }

  .intro { left: 59px; top: 144px; width: 305px; font-size: 15px; line-height: 17.4px; font-weight: 500; }
  .intro-checks { left: 58px; top: 210px; width: 290px; list-style: none; font-size: 13.8px; line-height: 16px; font-weight: 500; }
  .intro-checks li { position: relative; padding-left: 25px; }
  .intro-checks svg { position: absolute; left: 0; top: 1px; width: 12px; height: 12px; }
  .intro-note { left: 85px; top: 280px; width: 260px; font-size: 14.6px; line-height: 17px; font-weight: 800; font-style: italic; }

  .side-panel { left: 378px; top: 147px; width: 347px; height: 803px; background: var(--navy); border-radius: 24px; }
  .caution-band { left: 391px; top: 165px; width: 365px; height: 33px; background: var(--green); border-radius: 5px 0 0 5px; color: var(--white); font-weight: 800; font-size: 17.5px; line-height: 33px; padding-left: 110px; }
  .caution-text { left: 405px; top: 212px; width: 300px; color: var(--white); font-size: 14px; line-height: 15.9px; font-weight: 400; }

  .drug-table { left: 48px; top: 343px; width: 695px; height: 324px; background: var(--white); border: 2.5px solid var(--green); border-radius: 22px; }
  .drug-table > * { position: absolute; }
  .th { top: 17px; height: 34px; border-radius: 5px; color: var(--white); font-weight: 700; font-size: 15.5px; line-height: 34px; text-align: center; }
  .th-action { left: 17px; width: 176px; background: var(--navy); }
  .th-drug { left: 197px; width: 475px; background: var(--green); }
  .row-bg { border-radius: 8px; background: var(--cell); }
  .action { left: 37px; font-size: 14px; line-height: 16px; font-weight: 500; }
  .drugs { left: 240px; width: 400px; list-style: none; font-size: 14px; line-height: 16px; font-weight: 500; }
  .drugs li { position: relative; padding-left: 22px; }
  .drugs li + li { margin-top: 8px; }
  .drugs svg { position: absolute; left: 0; top: 1px; width: 13px; height: 12px; }

  .refractory { left: 55px; top: 692px; width: 300px; text-align: center; font-weight: 800; font-size: 21px; line-height: 25px; }

  .bp-title { left: 53px; top: 786px; width: 303px; height: 30px; background: var(--green); color: var(--white); font-weight: 700; font-size: 14.6px; line-height: 30px; text-align: center; border-radius: 2px; }
  .bp-grid { left: 53px; top: 822px; width: 303px; display: grid; grid-template-columns: 90px 103px 102px; column-gap: 4px; row-gap: 6px; }
  .bp-grid span { height: 28px; background: var(--cell); text-align: center; line-height: 28px; font-size: 14.4px; font-weight: 400; border-radius: 2px; }
  .bp-grid .bp-head { font-weight: 700; font-size: 14.8px; background: #f1f1f1; }

  .diff-title { left: 405px; top: 687px; color: var(--green); font-weight: 800; font-size: 17px; }
  .diff-list { left: 406px; top: 716px; width: 290px; list-style: none; color: var(--white); font-size: 14.4px; line-height: 18.8px; font-weight: 500; }
  .diff-list li { position: relative; padding-left: 24px; }
  .diff-list svg { position: absolute; left: 0; top: 4px; width: 12px; height: 11px; }
</style>
</head>
<body>
<svg width="0" height="0" style="position:absolute">
  <defs>
    <symbol id="tick" viewBox="0 0 12 11"><path d="M1 6 L4.5 9.5 L11 1.5" fill="none" stroke="currentColor" stroke-width="2.6" stroke-linecap="round" stroke-linejoin="round"/></symbol>
  </defs>
</svg>

<main class="page">
  <div class="spine"></div>
  <div class="top-band"></div>

  <h1 class="title">HYPERTENSION, <span class="accent">ACUTE</span></h1>

  <p class="intro">In pediatrics, hypertension is almost always treated by addressing likely causes such as light anesthesia or measurement error:</p>
  <ul class="intro-checks">
    <li><svg style="color:var(--green)"><use href="#tick"/></svg>Ensure correct BP cuff size: cuff bladder width ~ 40% of limb circumference</li>
    <li><svg style="color:var(--green)"><use href="#tick"/></svg>Ensure arterial line transducer is at level of heart</li>
  </ul>
  <p class="intro-note">( Consider placing arterial line if not already present )</p>

  <div class="side-panel"></div>
  <div class="caution-band">* CAUTION:</div>
  <p class="caution-text">Anti-hypertensive drugs are almost never needed for routine pediatric cases. These medications are used almost exclusively for specialized cardiac, neurosurgical, or endocrine (pheochromocytoma) cases. Consult an expert before use. Rule-out increased ICP.</p>

  <section class="drug-table">
    <div class="th th-action">Action</div>
    <div class="th th-drug">Drug (IV Dosing)</div>

    <div class="row-bg" style="left:17px;top:118px;width:176px;height:88px"></div>
    <div class="row-bg" style="left:197px;top:118px;width:475px;height:88px"></div>
    <div class="row-bg" style="left:17px;top:268px;width:176px;height:32px"></div>
    <div class="row-bg" style="left:197px;top:268px;width:475px;height:32px"></div>

    <p class="action" style="top:69px">Direct smooth<br>muscle relaxation</p>
    <ul class="drugs" style="top:62px">
      <li><svg style="color:var(--orange)"><use href="#tick"/></svg>Sodium nitroprusside 0.5-10 MICROgrams/kg/min</li>
      <li><svg style="color:var(--orange)"><use href="#tick"/></svg>HydrALAZINE 0.1-0.2 mg/kg (adult dose 5-10 mg)</li>
    </ul>

    <p class="action" style="top:146px">Adrenergic<br>blockade</p>
    <ul class="drugs" style="top:126px">
      <li><svg style="color:var(--orange)"><use href="#tick"/></svg>Esmolol 100-500 MICROgrams/kg over 5 min, then<br>25-300 MICROgrams/kg/min</li>
      <li><svg style="color:var(--orange)"><use href="#tick"/></svg>Labetalol (also α effect) 0.2-1 mg/kg q 10 min; 0.4-3 mg/<br>kg/hour (infusion)</li>
    </ul>

    <p class="action" style="top:222px">Calcium channel<br>blockade</p>
    <ul class="drugs" style="top:218px">
      <li><svg style="color:var(--orange)"><use href="#tick"/></svg>niCARdapine 0.5-5 MICROgrams/kg/min</li>
      <li><svg style="color:var(--orange)"><use href="#tick"/></svg>Clevidipine 0.5-3.5 MICROgrams/kg/min</li>
    </ul>

    <p class="action" style="top:276px">D1-dopamine agonist</p>
    <ul class="drugs" style="top:276px">
      <li><svg style="color:var(--orange)"><use href="#tick"/></svg>Fenoldopam 0.2-0.8 MICROgrams/kg/min</li>
    </ul>
  </section>

  <h2 class="refractory">Sustained high blood pressure refractory to treating reversible causes</h2>

  <div class="bp-title">Hypertensive Blood Pressure Range*</div>
  <div class="bp-grid">
    <span class="bp-head">Age (yr)</span><span class="bp-head">Systolic</span><span class="bp-head">Diastolic</span>
    <span>newborn</span><span>&gt;97</span><span>&gt;70</span>
    <span>1-3</span><span>&gt;105</span><span>&gt;61</span>
    <span>4-12</span><span>&gt;113</span><span>&gt;86</span>
  </div>

  <h3 class="diff-title">Consider Differential (Partial):</h3>
  <ul class="diff-list">
    <li><svg style="color:var(--white)"><use href="#tick"/></svg>Light anesthesia (consider vaporizer or infusion pump empty or malfunctioning)</li>
    <li><svg style="color:var(--white)"><use href="#tick"/></svg>Hypercarbia</li>
    <li><svg style="color:var(--white)"><use href="#tick"/></svg>Hypoxemia</li>
    <li><svg style="color:var(--white)"><use href="#tick"/></svg>Arterial line transducer too low or BP cuff too small</li>
    <li><svg style="color:var(--white)"><use href="#tick"/></svg>Withdrawal (EtOH or opioid)</li>
    <li><svg style="color:var(--white)"><use href="#tick"/></svg>Thyroid Storm</li>
    <li><svg style="color:var(--white)"><use href="#tick"/></svg>Pheochromocytoma</li>
    <li><svg style="color:var(--white)"><use href="#tick"/></svg>Drug Error</li>
  </ul>
</main>
</body>
</html>
```